Building Company Business Card Design

Need a design for a business card:
It needs to have: Name, Phone, Facebook link, Website, email
i would also like a list of works we undertake:
-New Homes
-Extensions, Renovations & Bathrooms
-Decking, Carports, Sheds (Residential and Industrial)
-Carpentry
-Fences, Patios & Pergolas

Name, Phone, Facebook link, Website, email + details of services provided listed in description

```html
<!DOCTYPE html>
<html lang="en">
<head>
<meta charset="utf-8">
<title>Ridgeline Homes – Business Card</title>
<link href="https://fonts.googleapis.com/css2?family=Montserrat:wght@400;500;600;700&display=swap" rel="stylesheet">
<style>
  :root {
    --backdrop: #9b9b9b;
    --paper: #f7f7f6;
    --card-dark: #1b1b1b;
    --green: #2fb64a;
    --green-edge: #1f9a2f;
    --ink: #3a3a3a;
    --ink-soft: #6a6a6a;
    --on-dark: #f2f2f2;
    --on-dark-soft: #a8a8a8;
  }
  * { margin: 0; padding: 0; box-sizing: border-box; }
  html, body { width: 1200px; height: 956px; overflow: hidden; }
  body {
    background: var(--backdrop);
    font-family: "Montserrat", sans-serif;
    display: flex;
    flex-direction: column;
    align-items: center;
    justify-content: center;
    gap: 40px;
  }
  .card {
    width: 720px;
    height: 410px;
    position: relative;
    border-bottom: 5px solid var(--green-edge);
    box-shadow: 0 10px 24px rgba(0,0,0,0.25);
  }
  .card-front { background: var(--paper); }
  .card-back { background: var(--card-dark); }

  .brand {
    position: absolute;
    left: 0; right: 0;
    display: flex;
    flex-direction: column;
    align-items: center;
    text-align: center;
  }
  .brand-row { display: flex; align-items: center; gap: 10px; }
  .brand-square { width: 26px; height: 26px; background: var(--green); }
  .brand-name {
    font-weight: 600;
    font-size: 40px;
    letter-spacing: 1px;
    text-transform: uppercase;
    line-height: 1;
  }
  .brand-sub {
    font-weight: 600;
    font-size: 15px;
    letter-spacing: 2px;
    text-transform: uppercase;
    margin-top: 6px;
  }
  .card-front .brand { top: 70px; }
  .card-front .brand-name, .card-front .brand-sub { color: var(--ink); }
  .card-front .brand-sub { color: var(--ink-soft); }
  .card-back .brand { top: 100px; }
  .card-back .brand-name { color: var(--on-dark); }
  .card-back .brand-sub { color: var(--on-dark-soft); }

  .person {
    position: absolute;
    left: 70px; top: 225px;
    width: 270px;
    text-align: right;
  }
  .person-name {
    color: var(--green);
    font-weight: 700;
    font-size: 30px;
    letter-spacing: 2px;
    text-transform: uppercase;
  }
  .person-title {
    color: var(--ink-soft);
    font-size: 14px;
    letter-spacing: 2px;
    text-transform: uppercase;
    margin-top: 4px;
  }
  .divider {
    position: absolute;
    left: 370px; top: 220px;
    width: 1.5px; height: 120px;
    background: var(--green);
  }
  .contacts {
    position: absolute;
    left: 395px; top: 222px;
    list-style: none;
  }
  .contacts li {
    display: flex;
    align-items: center;
    gap: 10px;
    color: var(--ink);
    font-size: 15px;
    letter-spacing: 0.5px;
    height: 29px;
  }
  .contacts svg { width: 14px; height: 14px; flex: none; }

  .services {
    position: absolute;
    left: 0; right: 0; top: 250px;
    text-align: center;
    color: var(--on-dark);
    font-size: 16px;
    letter-spacing: 0.5px;
    line-height: 34px;
  }
  .service { white-space: nowrap; }
  .service::before {
    content: "";
    display: inline-block;
    width: 9px; height: 9px;
    background: var(--green);
    margin: 0 8px 1px 12px;
  }
</style>
</head>
<body>

<section class="card card-front">
  <div class="brand">
    <div class="brand-row">
      <span class="brand-square"></span>
      <span class="brand-name">Ridgeline Homes</span>
    </div>
    <div class="brand-sub">and Developments Pty Ltd</div>
  </div>

  <div class="person">
    <div class="person-name">Daniel Reeve</div>
    <div class="person-title">Manager</div>
  </div>

  <div class="divider"></div>

  <ul class="contacts">
    <li>
      <svg viewBox="0 0 24 24" aria-hidden="true"><path fill="#2fb64a" d="M6.6 10.8a15.1 15.1 0 0 0 6.6 6.6l2.2-2.2a1 1 0 0 1 1-.25 11.4 11.4 0 0 0 3.6.57 1 1 0 0 1 1 1V20a1 1 0 0 1-1 1A17 17 0 0 1 3 4a1 1 0 0 1 1-1h3.5a1 1 0 0 1 1 1c0 1.25.2 2.45.57 3.57a1 1 0 0 1-.25 1z"/></svg>
      (555) 014-2287
    </li>
    <li>
      <svg viewBox="0 0 24 24" aria-hidden="true"><rect x="2" y="5" width="20" height="14" fill="#2fb64a"/><path d="M2 5l10 8 10-8" fill="none" stroke="#f7f7f6" stroke-width="1.8"/></svg>
      info@ridgelinehomes.example
    </li>
    <li>
      <svg viewBox="0 0 24 24" aria-hidden="true"><g fill="none" stroke="#2fb64a" stroke-width="2"><circle cx="12" cy="12" r="9.5"/><path d="M2.5 12h19M12 2.5c3 3 3 16 0 19M12 2.5c-3 3-3 16 0 19"/></g></svg>
      www.ridgelinehomes.example
    </li>
    <li>
      <svg viewBox="0 0 24 24" aria-hidden="true"><circle cx="12" cy="12" r="10" fill="#2fb64a"/></svg>
      @ridgelinehomesbuild
    </li>
  </ul>
</section>

<section class="card card-back">
  <div class="brand">
    <div class="brand-row">
      <span class="brand-square"></span>
      <span class="brand-name">Ridgeline Homes</span>
    </div>
    <div class="brand-sub">and Developments Pty Ltd</div>
  </div>

  <div class="services">
    <div><span class="service">New Homes</span><span class="service">Extensions, Renovations &amp; Bathrooms</span></div>
    <div><span class="service">Decking, Carports, Sheds</span><span class="service">Carpentry</span><span class="service">Fences, Patios &amp; Pergolas</span></div>
  </div>
</section>

</body>
</html>
```